Healthcare technology firm needs business card layout. Logo provided.

We need a business card design for a new healthcare technology company called Kevrimo.com. The logo is already done so that will be used in the design. We assist patients and their families manage their personal health finances. Our initial product is our web site membership that includes educational content on your health benefits, tools, and downloadable forms.

We would like to see designs that use our existing logo or extend the logo in a creative way. Should be very consumer friendly.

```html
<!DOCTYPE html>
<html lang="en">
<head>
<meta charset="utf-8">
<title>Kevrimo.com — Business Card Layout</title>
<link rel="stylesheet" href="https://fonts.googleapis.com/css2?family=Josefin+Sans:wght@400&family=PT+Sans:wght@400&display=swap">
<style>
  :root {
    --page-bg: #ffffff;
    --green-center: #7cbd2c;
    --green-edge: #16a34c;
    --blue-center: #1f7bcc;
    --blue-edge: #143f8c;
    --card-white: #ffffff;
    --logo-white: #ffffff;
    --brand-blue: #1a5fa8;
    --brand-green: #3aa64a;
    --ink: #333333;
    --muted: #666666;
    --card-shadow: 0 2px 8px rgba(0,0,0,0.35);
  }
  html, body {
    margin: 0;
    padding: 0;
    width: 1200px;
    height: 900px;
    overflow: hidden;
    background: var(--page-bg);
  }
  .sheet {
    position: relative;
    width: 1200px;
    height: 900px;
  }
  .card {
    position: absolute;
    width: 369px;
    height: 238px;
    box-shadow: var(--card-shadow);
    overflow: hidden;
  }
  .card--green { background: radial-gradient(ellipse at 50% 55%, var(--green-center) 0%, var(--green-edge) 80%); }
  .card--blue { background: radial-gradient(ellipse at 50% 50%, var(--blue-center) 0%, var(--blue-edge) 85%); }
  .card--white { background: var(--card-white); font-family: "PT Sans", sans-serif; }

  .front-a-green { left: 75px; top: 75px; }
  .front-b-green { left: 154px; top: 321px; }
  .back-green-labels { left: 231px; top: 567px; }
  .front-a-blue { left: 600px; top: 71px; }
  .front-b-blue { left: 676px; top: 318px; }
  .back-blue-labels { left: 755px; top: 564px; }

  .front-wordmark {
    position: absolute;
    left: 0;
    right: 0;
    top: 92px;
    text-align: center;
    font-family: "Josefin Sans", sans-serif;
    font-weight: 400;
    font-size: 42px;
    letter-spacing: 1px;
    color: var(--logo-white);
    line-height: 1;
  }

  .back-logo {
    position: absolute;
    left: 22px;
    top: 20px;
    white-space: nowrap;
  }
  .back-logo__name {
    font-family: "PT Sans", sans-serif;
    font-weight: 400;
    font-size: 36px;
    color: var(--brand-blue);
    letter-spacing: 0.5px;
  }
  .back-logo__tld {
    font-size: 13px;
    color: var(--muted);
    margin-left: 3px;
  }

  .holder {
    position: absolute;
    right: 22px;
    top: 77px;
    text-align: right;
  }
  .holder__name { font-size: 16px; color: var(--ink); line-height: 20px; }
  .holder__role { font-size: 11px; color: var(--ink); line-height: 18px; }

  .contact {
    position: absolute;
    left: 23px;
    top: 156px;
    margin: 0;
    padding: 0;
    list-style: none;
    font-size: 13px;
    line-height: 21px;
    color: var(--ink);
  }
  .contact__label { font-size: 12px; }
  .back-green-labels .contact__label { color: var(--brand-blue); }
  .back-blue-labels .contact__label { color: var(--brand-green); }
</style>
</head>
<body>
<main class="sheet">
  <section class="card card--green front-a-green"><div class="front-wordmark">KEVRIMO</div></section>
  <section class="card card--green front-b-green"><div class="front-wordmark">KEVRIMO</div></section>
  <section class="card card--white back-green-labels">
    <div class="back-logo"><span class="back-logo__name">Kevrimo</span><span class="back-logo__tld">.com</span></div>
    <div class="holder"><div class="holder__name">Nora Baines</div><div class="holder__role">Director</div></div>
    <ul class="contact">
      <li><span class="contact__label">Address</span> 214 Alder Lane</li>
      <li><span class="contact__label">Phone number</span> 555.018.2047</li>
      <li><span class="contact__label">E-mail</span> nora@kevrimo.com</li>
    </ul>
  </section>

  <section class="card card--blue front-a-blue"><div class="front-wordmark">KEVRIMO</div></section>
  <section class="card card--blue front-b-blue"><div class="front-wordmark">KEVRIMO</div></section>
  <section class="card card--white back-blue-labels">
    <div class="back-logo"><span class="back-logo__name">Kevrimo</span><span class="back-logo__tld">.com</span></div>
    <div class="holder"><div class="holder__name">Nora Baines</div><div class="holder__role">Director</div></div>
    <ul class="contact">
      <li><span class="contact__label">Address</span> 214 Alder Lane</li>
      <li><span class="contact__label">Phone number</span> 555.018.2047</li>
      <li><span class="contact__label">E-mail</span> nora@kevrimo.com</li>
    </ul>
  </section>
</main>
</body>
</html>
```